Oil and Gas Exploration and Production company needs a business card design

We need a business card design using our logo and colors in the logo. We want a mainstream design.

```html
<!DOCTYPE html>
<html lang="en">
<head>
<meta charset="UTF-8">
<title>Ridgeway Oil &amp; Gas – Business Card</title>
<link href="https://fonts.googleapis.com/css2?family=Cinzel:wght@600;700&family=Open+Sans:wght@400;600&display=swap" rel="stylesheet">
<style>
  :root {
    --stage: #3b3b3d;
    --card: #1f1f21;
    --card-edge: #2a2a2c;
    --gold: #d9a12b;
    --white: #f2f2f2;
    --muted: #8a8a8a;
  }
  * { box-sizing: border-box; margin: 0; padding: 0; }
  html, body { width: 1200px; height: 717px; overflow: hidden; }
  body {
    background: var(--stage);
    font-family: "Open Sans", sans-serif;
    display: flex;
    align-items: center;
    justify-content: center;
    gap: 60px;
  }
  .card {
    width: 520px;
    height: 297px;
    background: var(--card);
    border: 1px solid var(--card-edge);
    border-radius: 10px;
    position: relative;
    overflow: hidden;
  }
  .wordmark {
    display: flex;
    align-items: center;
    gap: 12px;
    font-family: "Cinzel", serif;
    font-weight: 700;
    color: var(--white);
    line-height: 1;
  }
  .wordmark .dot {
    border-radius: 50%;
    background: var(--gold);
    flex-shrink: 0;
  }
  .card-front { display: flex; align-items: center; justify-content: center; }
  .card-front .wordmark { font-size: 36px; color: #bdbdbd; }
  .card-front .dot { width: 30px; height: 30px; }

  .card-back .wordmark {
    position: absolute;
    top: 34px;
    right: 36px;
    font-size: 28px;
  }
  .card-back .dot { width: 24px; height: 24px; }
  .rule {
    position: absolute;
    left: 0; right: 0;
    height: 3px;
    background: var(--gold);
  }
  .rule-top { top: 92px; }
  .rule-bottom { top: 252px; }
  .identity {
    position: absolute;
    top: 110px;
    left: 34px;
    display: flex;
    align-items: center;
    gap: 14px;
  }
  .identity .name {
    font-family: "Cinzel", serif;
    font-weight: 600;
    font-size: 20px;
    color: var(--white);
    letter-spacing: 0.5px;
  }
  .identity .bar { width: 2px; height: 24px; background: var(--white); }
  .identity .role {
    font-family: "Cinzel", serif;
    font-weight: 700;
    font-size: 15px;
    color: var(--gold);
  }
  .details {
    position: absolute;
    top: 160px;
    left: 34px;
    right: 30px;
    display: flex;
    gap: 18px;
    font-size: 13px;
    color: var(--white);
  }
  .contacts { display: flex; flex-direction: column; gap: 5px; }
  .contact { display: flex; align-items: center; justify-content: flex-end; gap: 8px; }
  .divider { width: 2px; background: var(--muted); align-self: stretch; }
  .address { display: flex; gap: 8px; line-height: 1.35; }
  .icon { width: 14px; height: 14px; flex-shrink: 0; }
</style>
</head>
<body>
  <section class="card card-front" aria-label="Card front">
    <div class="wordmark"><span class="dot"></span>Ridgeway Oil &amp; Gas</div>
  </section>

  <section class="card card-back" aria-label="Card back">
    <div class="wordmark"><span class="dot"></span>Ridgeway Oil &amp; Gas</div>
    <div class="rule rule-top"></div>
    <div class="identity">
      <span class="name">Dale Harmon</span>
      <span class="bar"></span>
      <span class="role">CEO</span>
    </div>
    <div class="details">
      <div class="contacts">
        <div class="contact">1 555-014-2290
          <svg class="icon" viewBox="0 0 14 14"><circle cx="7" cy="7" r="7" fill="#d9a12b"/><path d="M4 5.5c0-1 .8-1.5 1.4-1.5l.8 1.6-.7.8c.4.9 1.1 1.6 2 2l.8-.7 1.6.8c0 .6-.5 1.4-1.5 1.4C6 9.9 4.1 8 4 5.5z" fill="#1f1f21"/></svg>
        </div>
        <div class="contact">+1 555-014-7731
          <svg class="icon" viewBox="0 0 14 14"><circle cx="7" cy="7" r="7" fill="#d9a12b"/><rect x="5" y="3.5" width="4" height="7" rx="0.8" fill="#1f1f21"/></svg>
        </div>
        <div class="contact">info@ridgewayoil.com
          <svg class="icon" viewBox="0 0 14 14"><circle cx="7" cy="7" r="7" fill="#d9a12b"/><rect x="3.5" y="4.5" width="7" height="5" fill="#1f1f21"/><path d="M3.5 4.5 7 7.3l3.5-2.8" stroke="#d9a12b" stroke-width="0.8" fill="none"/></svg>
        </div>
      </div>
      <div class="divider"></div>
      <div class="address">
        <svg class="icon" viewBox="0 0 14 14"><circle cx="7" cy="7" r="7" fill="#d9a12b"/><path d="M7 3a2.5 2.5 0 0 0-2.5 2.5C4.5 7.5 7 11 7 11s2.5-3.5 2.5-5.5A2.5 2.5 0 0 0 7 3z" fill="#1f1f21"/></svg>
        <p>PO Box:, Midland, TX,<br>USA, Odessa, TX 79760-0418<br>Box : 0418</p>
      </div>
    </div>
    <div class="rule rule-bottom"></div>
  </section>
</body>
</html>
```